Business Cards Needed for Innovative Healthcare Marketing Company

We are a marketing company focused on healthcare. Our company is all about rebranding yourself renewing your image and generating results. The phoenix stands for "reborn" or "rising" which we provide new brands for our clients we take their old brands and renew it with creativity and innovation. I am looking for a business card with color dimension. I have attached an example of a card I think has the look and feel of what I am trying to accomplish. I like that the card example has black and grey font colors, I like the font placement and the small logo, I really like the use of the colors on the right those are the colors of my logo. My logo is phoenix so maybe incorporating flames similar to that design. I would like the back a solid color maybe red with an opaque version of the logo and website. As a marketing company I am always open to creative liberty!

Target Market(s)

Doctors and business professionals.

Industry/Entity Type

Marketing

Contact Information for Business Card

Vornaly Health Care Marketing
Marnie Okonski- CEO
#(502)638-2947
email-marnie@vornaly.com
website- vornaly.com

Font styles to use
Sans Serif

Colors
ec1f27
f37122
ffc214
fbed22
fbf289
f04a50

Requirements
Must have
• The logo and required information
Nice to have
• icons by the information
Should not have
• child like font

```html
<!DOCTYPE html>
<html lang="en">
<head>
<meta charset="utf-8">
<title>Vornaly Health Care Marketing – Business Card</title>
<link href="https://fonts.googleapis.com/css2?family=Open+Sans:wght@400;600&display=swap" rel="stylesheet">
<style>
  :root {
    --stage: #d9d6d0;
    --card-black: #050505;
    --band-white: #ececec;
    --yellow-top: #e8cf1f;
    --yellow-bottom: #fbc21a;
    --brand-red: #d8262e;
    --brand-orange: #f37122;
    --ink: #0b0b0b;
    --icon-bg: #ffffff;
  }
  * { box-sizing: border-box; margin: 0; padding: 0; }
  html, body { width: 1200px; height: 892px; overflow: hidden; }
  body {
    background: var(--stage);
    display: flex;
    flex-direction: column;
    align-items: center;
    justify-content: center;
    gap: 32px;
  }
  .card {
    position: relative;
    width: 700px;
    height: 400px;
    overflow: hidden;
    box-shadow: 0 6px 18px rgba(0,0,0,.25);
    background: var(--card-black);
  }

  /* Front */
  .front-top { position: absolute; inset: 0 0 auto 0; height: 172px; background: var(--card-black); }
  .front-band { position: absolute; left: 0; right: 0; top: 172px; height: 16px; background: var(--band-white); }
  .front-info {
    position: absolute; left: 0; right: 0; top: 188px; bottom: 0;
    background: linear-gradient(90deg, var(--yellow-top), var(--yellow-bottom));
  }
  .person {
    position: absolute; left: 40px; top: 42px; width: 280px;
    text-align: center;
    font-family: "Open Sans", sans-serif; font-weight: 400;
    color: var(--ink);
  }
  .person-name { font-size: 30px; line-height: 1.2; }
  .person-title { font-size: 26px; line-height: 1.2; }
  .divider {
    position: absolute; left: 344px; top: 30px; width: 2px; height: 150px;
    background: var(--icon-bg);
  }
  .contacts {
    position: absolute; left: 384px; top: 40px;
    list-style: none;
    font-family: "Open Sans", sans-serif; font-weight: 600;
    font-size: 22px; color: var(--ink);
  }
  .contact { display: flex; align-items: center; gap: 14px; height: 44px; }
  .contact-icon {
    width: 24px; height: 24px; background: var(--icon-bg);
    display: flex; align-items: center; justify-content: center;
  }
  .contact-icon svg { width: 16px; height: 16px; }

  /* Company name placeholder */
  .company {
    position: absolute;
    display: flex; align-items: center; gap: 18px;
    font-family: "Open Sans", sans-serif; font-weight: 600;
    color: var(--brand-red);
    white-space: nowrap;
  }
  .company-dot { border-radius: 50%; background: var(--brand-orange); flex: none; }
  .company-name { line-height: 1; }

  .front-top .company { right: 40px; top: 60px; }
  .front-top .company-dot { width: 48px; height: 48px; }
  .front-top .company-name { font-size: 46px; }

  .card-back .company { left: 70px; top: 130px; }
  .card-back .company-dot { width: 80px; height: 80px; }
  .card-back .company-name { font-size: 72px; }

  .back-band {
    position: absolute; left: 0; right: 0; bottom: 28px; height: 30px;
    background: linear-gradient(90deg, var(--yellow-top), var(--yellow-bottom));
  }
</style>
</head>
<body>
  <section class="card card-front" aria-label="Business card front">
    <div class="front-top">
      <div class="company">
        <span class="company-dot"></span>
        <span class="company-name">Vornaly</span>
      </div>
    </div>
    <div class="front-band"></div>
    <div class="front-info">
      <div class="person">
        <p class="person-name">Marnie Okonski</p>
        <p class="person-title">CEO</p>
      </div>
      <div class="divider"></div>
      <ul class="contacts">
        <li class="contact">
          <span class="contact-icon">
            <svg viewBox="0 0 16 16"><path d="M4 1.5 6.2 4 5 5.6c.8 1.9 2.4 3.5 4.3 4.3L11 8.7 13.5 11 12 14c-5.5-.4-9.6-4.5-10-10Z" fill="#0b0b0b"/></svg>
          </span>
          #(502)638-2947
        </li>
        <li class="contact">
          <span class="contact-icon">
            <svg viewBox="0 0 16 16"><circle cx="8" cy="8" r="6" fill="none" stroke="#0b0b0b" stroke-width="1.6"/><path d="M2 8h12M8 2c-2.5 3.5-2.5 8.5 0 12M8 2c2.5 3.5 2.5 8.5 0 12" fill="none" stroke="#0b0b0b" stroke-width="1.2"/></svg>
          </span>
          vornaly.com
        </li>
        <li class="contact">
          <span class="contact-icon">
            <svg viewBox="0 0 16 16"><rect x="1.5" y="3.5" width="13" height="9" fill="#0b0b0b"/><path d="M1.5 3.5 8 9l6.5-5.5" fill="none" stroke="#fff" stroke-width="1.2"/></svg>
          </span>
          marnie@vornaly.com
        </li>
      </ul>
    </div>
  </section>

  <section class="card card-back" aria-label="Business card back">
    <div class="company">
      <span class="company-dot"></span>
      <span class="company-name">Vornaly</span>
    </div>
    <div class="back-band"></div>
  </section>
</body>
</html>
```